political campaign lawn sign - Governor's Council in Massachuesetts

We are looking for a political lawn sign. We are running a campaign for Governor's Council in Massachusetts. This sign will be on the lawn of homes and businesses so people driving by will see it. It needs to be simple and bold. The last name is long so maybe it could say vote for Carl and then Malbonske will be big a bold on the next line??
We need it to say:
Vote for Carlton Malbonske
Governor's Council.

Target Market(s)

local residents

Industry/Entity Type

Politcal Campaign

Font styles to use
Sans Serif
Other font styles liked:
• not sure what font but a modern looking one such as Helvetica, Arial, Sans Seri, sharp sans..

Colors
0054AA
0677BA
7BADD7
CADEEF
E8F1F8
00AB8E
00BBA5
67D7C9
C6EFE9
E9F9F6
FFF300
FFF600
FEFA6F
FFFEC7
FFFEE8

Requirements
Must have
• My name written out with a Capital D and R but lower case for every other letter so its Carl Malbonske
Nice to have
• modern font , the Colors of the lawn sign should have Blue, Yellow and White something bold that will stand out
Should not have
• any maps of Massachusetts

```html
<!DOCTYPE html>
<html lang="en">
<head>
<meta charset="utf-8">
<title>Vote for Carlton Malbonske – Governor's Council Lawn Sign</title>
<link rel="stylesheet" href="https://fonts.googleapis.com/css2?family=Montserrat:wght@600;700;800&family=Source+Serif+4:ital,wght@1,700&display=swap">
<style>
  :root {
    --sign-blue: #0054AA;
    --sign-yellow: #FFF300;
    --sign-white: #FFFFFF;
    --page-bg: #FFFFFF;
  }
  html, body {
    margin: 0;
    padding: 0;
    width: 1200px;
    height: 1000px;
    overflow: hidden;
    background: var(--page-bg);
  }
  .lawn-sign {
    display: block;
    width: 1200px;
    height: 1000px;
  }
  .sign-panel { fill: var(--sign-blue); }
  .frame-bracket { fill: none; stroke: var(--sign-yellow); stroke-width: 8; }
  .accent-star { fill: var(--sign-yellow); }
  .headline-vote {
    font-family: "Montserrat", sans-serif;
    font-weight: 700;
    font-size: 91px;
    fill: var(--sign-white);
  }
  .headline-for {
    font-family: "Source Serif 4", serif;
    font-style: italic;
    font-weight: 700;
    font-size: 44px;
    fill: var(--sign-yellow);
  }
  .candidate-name {
    font-family: "Montserrat", sans-serif;
    font-weight: 700;
    fill: var(--sign-white);
  }
  .candidate-first { font-size: 120px; }
  .candidate-last { font-size: 132px; }
  .office-title {
    font-family: "Montserrat", sans-serif;
    font-weight: 600;
    font-size: 66px;
    fill: var(--sign-yellow);
  }
</style>
</head>
<body>
<svg class="lawn-sign" viewBox="0 0 1200 1000" xmlns="http://www.w3.org/2000/svg" role="img" aria-label="Lawn sign: Vote for Carlton Malbonske, Governor's Council">
  <rect class="sign-panel" x="216" y="212" width="768" height="576"/>

  <!-- yellow corner brackets -->
  <polyline class="frame-bracket" points="440,248 252,248 252,468"/>
  <polyline class="frame-bracket" points="760,248 948,248 948,484"/>
  <polyline class="frame-bracket" points="252,628 252,752 392,752"/>
  <polyline class="frame-bracket" points="808,752 948,752 948,628"/>

  <!-- stars -->
  <polygon class="accent-star" points="319,398 325.8,419 348,419 330,432 336.8,453 319,440 301.2,453 308,432 290,419 312.2,419"/>
  <polygon class="accent-star" points="880,398 886.8,419 909,419 891,432 897.8,453 880,440 862.2,453 869,432 851,419 873.2,419"/>

  <text class="headline-vote" x="600" y="308" text-anchor="middle">VOTE</text>
  <text class="headline-for" x="598" y="368" text-anchor="middle">for</text>

  <text class="candidate-name candidate-first" x="600" y="473" text-anchor="middle">Carlton</text>
  <text class="candidate-name candidate-last" x="248" y="595" textLength="704" lengthAdjust="spacingAndGlyphs">Malbonske</text>

  <text class="office-title" x="327" y="693" textLength="545" lengthAdjust="spacingAndGlyphs">GOVERNER’S</text>
  <text class="office-title" x="407" y="756" textLength="386" lengthAdjust="spacingAndGlyphs">COUNCIL</text>
</svg>
</body>
</html>
```